Breakthrough memory supplement needs an eye catching label design

Brightvale Goods, LLC needs an eye catching label design for Cortivane, an Advanced Brain and Memory Formula

Completed label designs should be saved as .EPS files with all fonts outlined.
We can also accept Adobe Photoshop or .JPG files at 300dpi.
All files MUST include the .0625 bleed on all sides.

Target Market(s)

people 45 and older that are noticing there memory is not as good as it once was

Industry/Entity Type

Supplement

Colors

Designer to choose colors to be used in the design.

Requirements
Must have
• Cortivane
• Advanced Brain and Memory Formula
Nice to have
• look sciencey/ medical
Should not have
• cutesy

```html
<!DOCTYPE html>
<html lang="en">
<head>
<meta charset="utf-8">
<title>Cortivane Label</title>
<link rel="stylesheet" href="https://fonts.googleapis.com/css2?family=Montserrat:wght@600;700;800&family=Roboto+Condensed:wght@400;700&family=Archivo+Black&display=swap">
<style>
  :root {
    --page-bg: #ebebeb;
    --label-white: #ffffff;
    --ink: #1a1a1a;
    --ink-soft: #333333;
    --brand-red: #e4202a;
    --accent-orange: #f26522;
    --green-light: #9ccc3c;
    --green-mid: #52bd72;
    --teal: #17a99b;
    --sky: #2ab4dc;
  }
  * { margin: 0; padding: 0; box-sizing: border-box; }
  html, body { width: 1200px; height: 1200px; overflow: hidden; background: var(--page-bg); }
  .label {
    position: absolute; left: 18px; top: 384px;
    width: 1294px; height: 481px;
    transform: scale(0.9); transform-origin: top left;
    background: var(--label-white);
    box-shadow: 0 18px 30px rgba(0,0,0,0.18);
    overflow: hidden;
    font-family: Arial, Helvetica, sans-serif;
    color: var(--ink);
  }
  .label-art { position: absolute; inset: 0; }
  .directions {
    position: absolute; left: 27px; top: 40px; width: 303px;
    font-size: 11.2px; line-height: 13px; text-align: justify;
  }
  .directions p + p { margin-top: 13px; }
  .directions b { font-weight: 700; }
  .fda-note {
    position: absolute; left: 28px; top: 328px; width: 256px; height: 39px;
    border: 1.5px solid var(--ink); padding: 2px 3px;
    font-size: 8px; line-height: 10.5px; font-weight: 700;
  }
  .distributor {
    position: absolute; left: 30px; top: 388px;
    font-family: "Roboto Condensed", sans-serif; font-weight: 700;
    font-size: 14.5px; line-height: 19px; color: var(--ink);
  }
  .front { position: absolute; left: 400px; top: 0; width: 492px; text-align: center; }
  .company {
    position: absolute; top: 108px; left: 0; width: 100%;
    font-family: Montserrat, sans-serif; font-weight: 700; font-size: 24px;
    color: var(--ink-soft); letter-spacing: 0.3px;
  }
  .product-name {
    position: absolute; top: 152px; left: 0; width: 100%;
    font-family: Montserrat, sans-serif; font-weight: 800; font-size: 74px;
    line-height: 90px; color: var(--brand-red); letter-spacing: -1px;
  }
  .tagline {
    position: absolute; top: 254px; left: 40px; width: 413px; height: 36px;
    background: var(--label-white); border-radius: 5px;
    font-family: Montserrat, sans-serif; font-weight: 700; font-size: 18px;
    line-height: 36px; color: var(--brand-red);
    white-space: nowrap; letter-spacing: -0.2px;
  }
  .category {
    position: absolute; top: 325px; left: 0; width: 100%;
    font-family: Montserrat, sans-serif; font-weight: 700; font-size: 19px;
    color: var(--label-white); letter-spacing: 0.3px;
  }
  .count {
    position: absolute; top: 372px; left: 202px; width: 88px; height: 76px;
    background: var(--label-white); border-radius: 50%;
    color: var(--brand-red); padding-top: 10px;
  }
  .count-num { font-family: Montserrat, sans-serif; font-weight: 700; font-size: 27px; line-height: 28px; }
  .count-unit { font-family: "Roboto Condensed", sans-serif; font-weight: 400; font-size: 16px; line-height: 18px; }
  .facts {
    position: absolute; left: 949px; top: 42px; width: 302px;
    border: 2.5px solid var(--ink); padding: 0 6px 2px;
    font-size: 12px; line-height: 13px;
  }
  .facts-title { font-family: "Archivo Black", sans-serif; font-size: 28.5px; line-height: 32px; }
  .facts-serving { border-bottom: 6px solid var(--ink); padding-bottom: 3px; }
  .facts-head { font-size: 10px; letter-spacing: -0.4px; padding: 2px 0 1px; border-bottom: 1.5px solid var(--ink); }
  .facts-row { position: relative; display: flex; border-bottom: 1px solid var(--ink); padding: 1px 0; }
  .facts-row .name { flex: 1; }
  .facts-row .amt { width: 60px; text-align: right; }
  .facts-row .dv { width: 24px; text-align: right; }
  .facts-row .amt.float { position: absolute; right: 24px; top: 1px; }
  .facts-row .dv.float { position: absolute; right: 0; top: 1px; }
  .facts-row.last { border-bottom: none; }
  .facts-end { border-top: 5px solid var(--ink); padding-top: 1px; }
  .other {
    position: absolute; left: 951px; top: 333px; width: 303px;
    font-size: 12px; line-height: 12.5px; text-align: justify;
  }
  .other .caps { font-weight: 700; letter-spacing: -0.3px; }
  .other .gap { margin-top: 14px; }
</style>
</head>
<body>
<div class="label">
  <svg class="label-art" viewBox="0 0 1294 481" width="1294" height="481">
    <defs>
      <linearGradient id="field" x1="0" y1="1" x2="1" y2="0.2">
        <stop offset="0" stop-color="#9ccc3c"/>
        <stop offset="0.35" stop-color="#52bd72"/>
        <stop offset="0.7" stop-color="#17a99b"/>
        <stop offset="1" stop-color="#2ab4dc"/>
      </linearGradient>
    </defs>
    <path role="img" aria-label="Neuron network background in green and teal"
          d="M186,481 C225,300 295,120 400,0 L1180,0 C1228,12 1266,30 1294,56 L1294,481 Z" fill="url(#field)"/>
    <path d="M206,382 C238,222 290,92 360,0 L386,0 C302,110 246,230 206,382 Z" fill="#f26522"/>
    <path d="M1226,0 L1294,0 L1294,40 C1276,22 1254,9 1226,0 Z" fill="#f26522"/>
  </svg>

  <div class="directions">
    <p><b>SUGGESTED USE:</b> 1 capsule taken 1 to 2 times daily preferably with meals or as directed by a healthcare professional.</p>
    <p><b>CAUTION:</b> Do not exceed recommended dose. St. John's Wort may contribute to photosensitivity resulting in skin irritation and redness in persons exposed to strong sunlight or tanning booths. Avoid use in patients at risk of bleeding, taking anticoagulants, or with clotting disorders, based on case reports of bleeding. Discontinue use 2-3 weeks prior to some surgical and dental procedures due to increased risk of bleeding. Avoid use in couples who are trying to conceive, based on theoretical reduction of fertility. Pregnant or nursing mothers, children under 18, individuals with history of seizure, taking MAO inhibiting drugs, or with a known medical condition should consult a physician before using this or any dietary supplement. This product is manufactured and packaged in a facility which may also process milk, soy, wheat, egg, peanuts, tree nuts, fish and crustacean shellfish.</p>
  </div>
  <div class="fda-note">†These statements have not been evaluated by the Food &amp; Drug Administration. This product is not intended to diagnose, treat, cure or prevent any disease.</div>
  <div class="distributor">Distributed by:<br>Company Name<br>Full Address and Phone</div>

  <div class="front">
    <div class="company">Brightvale Goods, LLC</div>
    <div class="product-name">Cortivane</div>
    <div class="tagline">an Advanced Brain and Memory Formula</div>
    <div class="category">DIETARY SUPPLEMENT</div>
    <div class="count"><div class="count-num">30</div><div class="count-unit">CAPSULES</div></div>
  </div>

  <div class="facts">
    <div class="facts-title">Supplement Facts</div>
    <div class="facts-serving">Serving Size 1 Capsule<br>Servings Per Container: 30</div>
    <div class="facts-head">Amt Per Serv. %DV/RDI</div>
    <div class="facts-row"><span class="name"><i>Ginkgo biloba</i> Leaf (24% extract)</span><span class="amt">50mg</span><span class="dv">*</span></div>
    <div class="facts-row"><span class="name">Phosphatidylserine 4% Complex<br>(consisting of Lecithin and Phosphatidylserine)</span><span class="amt float">125mg</span><span class="dv float">*</span></div>
    <div class="facts-row"><span class="name">N-Acetyl L-Carnitine HCl</span><span class="amt">50mg</span><span class="dv">*</span></div>
    <div class="facts-row"><span class="name">St. John's Wort (0.3% extract)<br>(flower heads)</span><span class="amt">250mg</span><span class="dv">*</span></div>
    <div class="facts-row"><span class="name">L-Glutamine</span><span class="amt">150mg</span><span class="dv">*</span></div>
    <div class="facts-row"><span class="name"><i>Bacopa monnieri</i> Leaf Extract<br>(20% bacosides)</span><span class="amt">120mg</span><span class="dv">*</span></div>
    <div class="facts-row"><span class="name">Vinpocetine (seeds)</span><span class="amt">2mg</span><span class="dv">*</span></div>
    <div class="facts-row last"><span class="name">Huperzine-A (aerial plant)</span><span class="amt">10mcg</span><span class="dv">*</span></div>
    <div class="facts-end">*Daily Value not established.</div>
  </div>

  <div class="other">
    <b>Other ingredients:</b> Gelatin (bovine), microcrystalline cellulose, vegetable magnesium stearate, and silicon dioxide.
    <div class="caps">ALLERGEN WARNING: CONTAINS SOY (LECITHIN).</div>
    <div class="caps gap">KEEP OUT OF THE REACH OF CHILDREN.<br>DO NOT USE IF SAFETY SEAL IS DAMAGED OR MISSING. STORE IN A COOL, DRY PLACE.</div>
  </div>
</div>
</body>
</html>
```